Business card design needed

We need a business card design for a new consulting business based in Melbourne called Harbourline Advisory Group. Our tag line is 'Building Stronger Foundations'. We work with not for profits and Small - Medium Enterprises to provide advice and solutions around finance, governance, HR, IT and risk management. The idea around our organisation is to help charities and small businesses with their business foundations, so that they can spend more time focussing on their mission.
We have a logo designed already and would like the business card to use similar colours and themes - collaboration, having a conversation, creating impact. We would like the design to be eye catching but also convey professional credibility.
We would like a double sided card please.
Target Market(s)
CEOs and senior managers in charities and Small to Medium Enterprises
Industry/Entity Type
Business
Contact Information for Business Card
Business Name: Harbourline Advisory Group
Staff Member: Danielle Forsyth FCA
Title: Principal Consultant
Email address: danielle@harbourlineadvisorygroup.com.au
Phone: 03 9990 2874
Mobile: 0407 918 246
Address: PO Box 87, Wattlebrook VIC 3198
Web: www.harbourlineadvisorygroup.com.au
Linked In: connect.harbourlineadvisorygroup.com.au/danielle
Look and feel

```html
<!DOCTYPE html>
<html lang="en">
<head>
<meta charset="utf-8">
<title>Harbourline Advisory Group – Business Card</title>
<link rel="stylesheet" href="https://fonts.googleapis.com/css2?family=Questrial&family=Poppins:wght@600&display=swap">
<style>
  :root {
    --purple: #6b2d90;
    --cyan: #27b4e4;
    --ink: #4a4a4c;
    --charcoal: #3a3a3c;
    --card: #ffffff;
    --backdrop: #c9c9cb;
  }
  * { box-sizing: border-box; margin: 0; padding: 0; }
  html, body {
    width: 1200px; height: 675px; overflow: hidden;
    background: var(--backdrop);
    font-family: "Questrial", "Century Gothic", sans-serif;
    color: var(--ink);
  }
  .sheet {
    width: 1200px; height: 675px;
    display: flex; align-items: center; justify-content: center; gap: 48px;
  }
  .card {
    position: relative;
    width: 540px; height: 300px;
    background: var(--card);
    box-shadow: 0 6px 18px rgba(0,0,0,.18);
  }

  /* Brand lockup */
  .lockup { display: flex; align-items: center; gap: 14px; }
  .lockup__dot { flex: none; border-radius: 50%; background: var(--cyan); }
  .lockup__name {
    color: var(--purple);
    text-transform: uppercase;
    letter-spacing: .04em;
    line-height: 1;
    white-space: nowrap;
  }
  .lockup__tagline {
    color: var(--cyan);
    text-transform: uppercase;
    letter-spacing: .05em;
    line-height: 1;
    white-space: nowrap;
  }

  /* Front */
  .card--front { display: flex; align-items: center; justify-content: center; }
  .card--front .lockup__dot { width: 88px; height: 88px; }
  .card--front .lockup__name { font-size: 24px; }
  .card--front .lockup__tagline { font-size: 13px; margin-top: 8px; text-align: right; }

  /* Back */
  .card--back .lockup { position: absolute; left: 28px; top: 34px; gap: 10px; }
  .card--back .lockup__dot { width: 48px; height: 48px; }
  .card--back .lockup__name { font-size: 12.5px; }
  .card--back .lockup__tagline { font-size: 7.5px; margin-top: 5px; text-align: right; }

  .person {
    position: absolute; right: 28px; top: 30px; text-align: right;
  }
  .person__name {
    font-family: "Poppins", "Century Gothic", sans-serif;
    font-weight: 600; font-size: 13px; color: var(--charcoal);
  }
  .person__title { font-size: 9.5px; color: var(--purple); margin-top: 6px; }

  .rule { position: absolute; height: 1px; background: var(--purple); }
  .rule--top { left: 230px; right: 28px; top: 92px; }
  .rule--contact { left: 28px; width: 250px; top: 150px; }

  .contact {
    position: absolute; left: 28px; top: 162px;
    list-style: none; font-size: 11px; color: var(--ink);
  }
  .contact__address { margin-bottom: 9px; }
  .contact__row { display: flex; align-items: center; gap: 10px; height: 19px; white-space: nowrap; }
  .contact__icon { width: 11px; height: 11px; flex: none; color: var(--purple); }
</style>
</head>
<body>
<main class="sheet">

  <section class="card card--front" aria-label="Card front">
    <div class="lockup">
      <span class="lockup__dot" aria-hidden="true"></span>
      <div>
        <p class="lockup__name">Harbourline Advisory Group</p>
        <p class="lockup__tagline">Building Stronger Foundations</p>
      </div>
    </div>
  </section>

  <section class="card card--back" aria-label="Card back">
    <div class="lockup">
      <span class="lockup__dot" aria-hidden="true"></span>
      <div>
        <p class="lockup__name">Harbourline Advisory Group</p>
        <p class="lockup__tagline">Building Stronger Foundations</p>
      </div>
    </div>

    <div class="person">
      <p class="person__name">Danielle Forsyth FCA</p>
      <p class="person__title">Principal Consultant</p>
    </div>

    <span class="rule rule--top" aria-hidden="true"></span>
    <span class="rule rule--contact" aria-hidden="true"></span>

    <ul class="contact">
      <li class="contact__address">PO Box 87, Wattlebrook VIC 3198</li>
      <li class="contact__row">
        <svg class="contact__icon" viewBox="0 0 12 12" aria-hidden="true"><path fill="currentColor" d="M1 4c0-1.5 2-2.5 5-2.5S11 2.5 11 4l-2.5.6L8 3.4H4l-.5 1.2L1 4zm2 2h6l1 4.5H2L3 6zm3 .8a1.5 1.5 0 1 0 0 3 1.5 1.5 0 0 0 0-3z"/></svg>
        <span>03 9990 2874</span>
      </li>
      <li class="contact__row">
        <svg class="contact__icon" viewBox="0 0 12 12" aria-hidden="true"><rect x="3" y="0.5" width="6" height="11" rx="1.2" fill="none" stroke="currentColor" stroke-width="1.2"/><circle cx="6" cy="9.6" r=".8" fill="currentColor"/></svg>
        <span>0407 918 246</span>
      </li>
      <li class="contact__row">
        <svg class="contact__icon" viewBox="0 0 12 12" aria-hidden="true"><g fill="none" stroke="currentColor" stroke-width="1"><circle cx="6" cy="6" r="5"/><ellipse cx="6" cy="6" rx="2.2" ry="5"/><path d="M1 6h10M2 3.3h8M2 8.7h8"/></g></svg>
        <span>www.harbourlineadvisorygroup.com.au</span>
      </li>
      <li class="contact__row">
        <svg class="contact__icon" viewBox="0 0 12 12" aria-hidden="true"><g fill="none" stroke="currentColor" stroke-width="1.2" stroke-linecap="round"><path d="M5 7l2-2"/><path d="M6.5 3.5l1-1a2 2 0 0 1 2.8 2.8l-1 1"/><path d="M5.5 8.5l-1 1a2 2 0 0 1-2.8-2.8l1-1"/></g></svg>
        <span>connect.harbourlineadvisorygroup.com.au/danielle</span>
      </li>
    </ul>
  </section>

</main>
</body>
</html>
```